A start up special flyer design!

Hi All - Have updated the attachment content - This is the info required for the designs.
I need a catchy flyer to send out to a few areas to advertise the start of my plumbing business!
The flyer will contain an offer for customers, which will need to have some key details on it. See attached. Feel free to fit these criteria into the flyer given your knowledge on design and messaging principles. Key thing to get across to customers is the discount and special offer, and that it is a start up offer.
I have a logo that needs to be on the flyer as well - let me know what format you require and I will send through to you.
The color scheme needs to be blue / grey / black / white.
Let me know if you have any questions.
I

```html
<!DOCTYPE html>
<html lang="en">
<head>
<meta charset="utf-8">
<title>Ridgewater Plumbing – Start-up Flyer &amp; Business Cards</title>
<link rel="stylesheet" href="https://fonts.googleapis.com/css2?family=Roboto+Condensed:ital,wght@0,400;0,700;1,400;1,700&family=Open+Sans:wght@400;600&display=swap">
<style>
  :root{
    --bg:#e6e7e9;
    --blue:#1f6fb0;
    --blue-dark:#0b4f8c;
    --blue-light:#5fb3e2;
    --blue-pale:#9fd3f0;
    --navy:#2b4a8a;
    --grey:#9a9a9a;
    --grey-dark:#6f6f6f;
    --ink:#141414;
    --white:#ffffff;
  }
  *{box-sizing:border-box;margin:0;padding:0}
  html,body{width:1200px;height:1000px;overflow:hidden;background:var(--bg)}
  body{position:relative;font-family:"Roboto Condensed",Arial,sans-serif;color:var(--ink)}

  /* ---------- Flyer ---------- */
  .flyer{position:absolute;left:42px;top:88px;width:636px;height:824px;background:var(--white);overflow:hidden;box-shadow:0 2px 8px rgba(0,0,0,.18)}
  .flyer-shapes{position:absolute;inset:0}
  .abs{position:absolute}
  .banner-title{position:absolute;color:var(--white);font-weight:700;font-size:34px;line-height:1}
  .offer-list,.service-list{position:absolute;list-style:none;color:var(--white);font-size:19px;line-height:24px}
  .offer-list li,.service-list li{position:relative;padding-left:25px}
  .tick{position:absolute;left:0;top:0;width:22px;height:22px}
  .brand{position:absolute;left:24px;top:392px;color:var(--ink);font-weight:700;line-height:1}
  .brand .brand-main{display:block;font-size:48px;letter-spacing:-.5px}
  .brand .brand-sub{display:block;font-size:25px;letter-spacing:3px;margin-top:4px}
  .appointment{position:absolute;left:18px;top:559px;font-size:14.5px;line-height:18px;color:var(--ink)}
  .appointment strong{display:block;color:var(--blue-dark);font-size:18px;line-height:22px}
  .phone-line{position:absolute;left:18px;top:663px;display:flex;align-items:center;gap:6px;font-size:29px;font-weight:700}
  .contact-small{position:absolute;left:24px;top:696px;font-size:13px;line-height:16px;text-align:center;width:176px}
  .fineprint{position:absolute;left:18px;top:750px;font-size:9.5px;line-height:12.5px;font-style:italic}
  .fineprint b{font-weight:700}
  .burst{position:absolute;left:380px;top:610px;width:180px;height:180px}
  .burst-text{position:absolute;left:380px;top:610px;width:180px;height:180px;color:var(--blue);font-weight:700;text-align:center}
  .burst-pct{position:absolute;left:20px;top:30px;font-size:62px;letter-spacing:-2px;line-height:1}
  .burst-off{position:absolute;left:122px;top:54px;font-size:26px;transform:rotate(-90deg);transform-origin:left top;line-height:1;display:block;top:94px;left:132px}
  .burst-bill{position:absolute;left:18px;top:104px;width:144px;font-size:19px;line-height:20px}

  /* ---------- Cards ---------- */
  .card{position:absolute;width:436px;height:262px;overflow:hidden;box-shadow:0 2px 8px rgba(0,0,0,.18)}
  .card-front{left:705px;top:230px;background:var(--blue)}
  .card-front .card-brand{position:absolute;left:0;right:0;top:48px;text-align:center;color:#b3b7bb;font-weight:700;line-height:1}
  .card-front .card-brand span{display:block}
  .card-front .card-brand .brand-main{font-size:58px}
  .card-front .card-brand .brand-sub{font-size:22px;letter-spacing:4px;margin-top:4px}
  .card-front .card-services{position:absolute;left:0;right:0;top:225px;text-align:center;color:#dfe9f3;font-size:13.5px;letter-spacing:.3px}
  .card-back{left:705px;top:515px;background:var(--white)}
  .card-back .card-brand{position:absolute;left:25px;top:20px;color:var(--ink);font-weight:700;line-height:1}
  .card-back .card-brand .brand-main{display:block;font-size:34px}
  .card-back .card-brand .brand-sub{display:block;font-size:15px;letter-spacing:3px;margin-top:2px}
  .card-rule{position:absolute;left:25px;right:19px;top:126px;height:1px;background:var(--grey)}
  .card-name{position:absolute;right:19px;top:104px;font-family:"Open Sans",Arial,sans-serif;color:var(--navy);font-size:16px}
  .card-role{position:absolute;right:19px;top:130px;font-family:"Open Sans",Arial,sans-serif;font-size:12.5px;color:#333}
  .card-contacts{position:absolute;left:25px;top:164px;list-style:none;font-family:"Open Sans",Arial,sans-serif;font-size:12px;color:#333;line-height:21px}
  .card-contacts li{display:flex;align-items:center;gap:6px}
  .card-contacts svg{width:13px;height:13px}
  .card-footer{position:absolute;left:0;bottom:0;width:436px;height:24px}
</style>
</head>
<body>

<!-- Flyer -->
<section class="flyer" aria-label="Start-up special flyer">
  <svg class="flyer-shapes" width="636" height="824" viewBox="0 0 636 824">
    <defs>
      <linearGradient id="panelGrad" x1="0" y1="0" x2="1" y2="1">
        <stop offset="0" stop-color="#2b8fd0"/>
        <stop offset=".55" stop-color="#6cc0ea"/>
        <stop offset="1" stop-color="#3d9ad6"/>
      </linearGradient>
      <linearGradient id="photoTop" x1="0" y1="0" x2="1" y2="1">
        <stop offset="0" stop-color="#3b5f95"/>
        <stop offset=".5" stop-color="#d9dde3"/>
        <stop offset="1" stop-color="#eef0f3"/>
      </linearGradient>
      <linearGradient id="photoMan" x1="0" y1="0" x2="0" y2="1">
        <stop offset="0" stop-color="#e9c36a"/>
        <stop offset=".25" stop-color="#3f63a8"/>
        <stop offset=".75" stop-color="#2c4f8e"/>
        <stop offset="1" stop-color="#8a6a44"/>
      </linearGradient>
    </defs>
    <!-- blue side panel -->
    <polygon points="403,0 636,0 636,824 325,824" fill="url(#panelGrad)"/>
    <!-- top photo area -->
    <polygon points="0,0 403,0 350,345 0,320" fill="url(#photoTop)" role="img" aria-label="Photo of a plumber in a blue cap fixing pipes under a sink"/>
    <polygon points="0,320 350,345 348,356 0,331" fill="var(--blue-dark)"/>
    <!-- banners -->
    <polygon points="348,75 598,75 608,127 341,127" fill="var(--blue-dark)"/>
    <polygon points="346,340 603,340 613,392 339,392" fill="var(--blue-dark)"/>
    <!-- smiling plumber photo area -->
    <rect x="208" y="427" width="185" height="397" rx="60" fill="url(#photoMan)" role="img" aria-label="Photo of a smiling plumber in a yellow hard hat with arms crossed and a tool belt"/>
    <!-- starburst -->
    <g transform="translate(470,700) rotate(-4)">
      <polygon fill="var(--white)" points="90,0 76.5,15.2 83.2,34.5 64.8,43.4 63.6,63.6 43.4,64.8 34.5,83.2 15.2,76.5 0,90 -15.2,76.5 -34.5,83.2 -43.4,64.8 -63.6,63.6 -64.8,43.4 -83.2,34.5 -76.5,15.2 -90,0 -76.5,-15.2 -83.2,-34.5 -64.8,-43.4 -63.6,-63.6 -43.4,-64.8 -34.5,-83.2 -15.2,-76.5 0,-90 15.2,-76.5 34.5,-83.2 43.4,-64.8 63.6,-63.6 64.8,-43.4 83.2,-34.5 76.5,-15.2"/>
    </g>
  </svg>

  <h2 class="banner-title" style="left:362px;top:84px">Special Offer</h2>
  <ul class="offer-list" style="left:398px;top:146px;width:220px">
    <li><svg class="tick" viewBox="0 0 22 22"><path d="M2 11 L8 18 L20 2" fill="none" stroke="var(--blue-dark)" stroke-width="3"/></svg>No GST payable, saving you additional 10% on your bill^</li>
    <li style="margin-top:26px"><svg class="tick" viewBox="0 0 22 22"><path d="M2 11 L8 18 L20 2" fill="none" stroke="var(--blue-dark)" stroke-width="3"/></svg>Plus, a FREE hot water health check and replacement quote~</li>
  </ul>

  <h2 class="banner-title" style="left:361px;top:349px">Services Offered</h2>
  <ul class="service-list" style="left:368px;top:409px;width:240px">
    <li><svg class="tick" viewBox="0 0 22 22"><path d="M2 11 L8 18 L20 2" fill="none" stroke="var(--blue-dark)" stroke-width="3"/></svg>All Plumbing, Draining, And Gasfitting Works</li>
    <li style="margin-top:23px"><svg class="tick" viewBox="0 0 22 22"><path d="M2 11 L8 18 L20 2" fill="none" stroke="var(--blue-dark)" stroke-width="3"/></svg>Quality Work At A Decent Price</li>
    <li style="margin-top:23px"><svg class="tick" viewBox="0 0 22 22"><path d="M2 11 L8 18 L20 2" fill="none" stroke="var(--blue-dark)" stroke-width="3"/></svg>Local Plumber</li>
  </ul>

  <div class="brand"><span class="brand-main">RIDGEWATER</span><span class="brand-sub">PLUMBING</span></div>

  <p class="appointment">To make an appointment,<strong>call or email Danny,</strong>or alternatively make a<br>booking directly on the website</p>

  <div class="phone-line">
    <svg width="24" height="24" viewBox="0 0 24 24"><circle cx="12" cy="12" r="10.5" fill="none" stroke="var(--blue)" stroke-width="2"/><path d="M8.5 7 l2 0 l1 3 l-1.5 1 a7 7 0 0 0 3 3 l1 -1.5 l3 1 l0 2 a2 2 0 0 1 -2 1.5 a10 10 0 0 1 -8 -8 a2 2 0 0 1 1.5 -2z" fill="var(--blue)"/></svg>
    <span>0412 555 018</span>
  </div>
  <p class="contact-small">danny@ridgewaterplumbing.com<br>www.ridgewaterplumbing.com</p>

  <p class="fineprint">*Offer valid between <b>15 August 2016 to 15 October 2016</b><br>^ Valid until <b>30 September 2016.</b><br>~ Quote valid for <b>12 months from the quote date.</b></p>

  <div class="burst-text">
    <span class="burst-pct">15%</span>
    <span class="burst-off">OFF</span>
    <span class="burst-bill">YOUR OVERALL BILL*</span>
  </div>
</section>

<!-- Business card, front -->
<section class="card card-front" aria-label="Business card front">
  <div class="card-brand"><span class="brand-main">RIDGEWATER</span><span class="brand-sub">PLUMBING</span></div>
  <p class="card-services">PLUMBING &nbsp;•&nbsp; DRAINING &nbsp;•&nbsp; GASFITTING WORKS</p>
</section>

<!-- Business card, back -->
<section class="card card-back" aria-label="Business card back">
  <div class="card-brand"><span class="brand-main">RIDGEWATER</span><span class="brand-sub">PLUMBING</span></div>
  <p class="card-name">Name</p>
  <div class="card-rule"></div>
  <p class="card-role">Designation</p>
  <ul class="card-contacts">
    <li><svg viewBox="0 0 14 14"><circle cx="7" cy="7" r="6" fill="none" stroke="var(--navy)" stroke-width="1.2"/><path d="M5 4 h1.2 l.6 1.8 l-.9 .6 a4 4 0 0 0 1.8 1.8 l.6 -.9 l1.8 .6 v1.2 a1 1 0 0 1 -1 .8 a6 6 0 0 1 -5 -5 a1 1 0 0 1 .9 -.9z" fill="var(--navy)"/></svg>0412 555 018</li>
    <li><svg viewBox="0 0 14 14"><rect x="1" y="3" width="12" height="8" fill="none" stroke="var(--navy)" stroke-width="1.2"/><path d="M1 3 L7 8 L13 3" fill="none" stroke="var(--navy)" stroke-width="1.2"/></svg>danny@ridgewaterplumbing.com</li>
    <li><svg viewBox="0 0 14 14"><circle cx="7" cy="7" r="6" fill="none" stroke="var(--navy)" stroke-width="1.2"/><ellipse cx="7" cy="7" rx="2.6" ry="6" fill="none" stroke="var(--navy)" stroke-width="1"/><path d="M1 7 H13" stroke="var(--navy)" stroke-width="1"/></svg>www.ridgewaterplumbing.com</li>
  </ul>
  <svg class="card-footer" viewBox="0 0 436 24">
    <polygon points="0,2 227,2 217,24 0,24" fill="var(--blue)"/>
    <polygon points="230,2 436,2 436,24 220,24" fill="var(--grey-dark)"/>
    <polygon points="0,0 436,0 436,2 0,2" fill="var(--white)"/>
  </svg>
</section>

</body>
</html>
```